BRISK GUARD WEBSITE BANNER DESIGN OF AWESOME

Please take a look at the attached Banner. I want a redesign Idea. The requirements are below.

1)Must Use Website Background
2)Must Use Photo Provided
3)Must Include Button
4)Website the banner will be used on you can see the current at the bottom of the page: https://b.plomvarn.com

Target Market(s)

Anyone Seeking Security Guard Services

```html
<!DOCTYPE html>
<html lang="en">
<head>
<meta charset="UTF-8">
<title>Brisk Guard – Get Secured Today</title>
<link href="https://fonts.googleapis.com/css2?family=Montserrat:wght@500;600;800&display=swap" rel="stylesheet">
<style>
  :root {
    --navy: #1d3461;
    --navy-deep: #111f3a;
    --steel: #5d7fa3;
    --wall: #9fb6cc;
    --beam: #f4c891;
    --orange: #f6a623;
    --white: #ffffff;
    --ink: #1f2f4f;
  }
  html, body {
    margin: 0;
    padding: 0;
    width: 1200px;
    height: 431px;
    overflow: hidden;
    background: var(--navy);
  }
  .banner {
    position: relative;
    width: 1200px;
    height: 431px;
    overflow: hidden;
    background: var(--navy);
    font-family: "Montserrat", Arial, sans-serif;
    color: var(--white);
  }
  .banner__photo {
    position: absolute;
    top: 0;
    left: 580px;
    width: 620px;
    height: 431px;
    background:
      radial-gradient(ellipse 170px 150px at 230px 40px, rgba(200,216,232,0.85), rgba(200,216,232,0) 75%),
      radial-gradient(ellipse 120px 60px at 330px 120px, rgba(244,200,145,0.75), rgba(244,200,145,0) 80%),
      radial-gradient(ellipse 80px 70px at 440px 70px, rgba(244,200,145,0.55), rgba(244,200,145,0) 80%),
      linear-gradient(160deg, transparent 55%, rgba(17,31,58,0.55) 75%),
      linear-gradient(200deg, #8aa6c2 0%, var(--steel) 30%, #34537a 60%, var(--navy-deep) 100%);
  }
  .banner__photo::before {
    content: "";
    position: absolute;
    inset: 0;
    background: linear-gradient(90deg, var(--navy) 0%, rgba(29,52,97,0.75) 10%, rgba(29,52,97,0) 30%);
  }
  .banner__photo::after {
    content: "";
    position: absolute;
    left: 20px;
    bottom: 0;
    width: 320px;
    height: 320px;
    background: radial-gradient(ellipse 170px 220px at 50% 100%, rgba(17,31,58,0.85), rgba(17,31,58,0) 80%);
  }
  .banner__brand {
    position: absolute;
    top: 64px;
    left: 1004px;
    font-weight: 800;
    font-size: 20px;
    letter-spacing: 1px;
    color: var(--white);
  }
  .banner__content {
    position: absolute;
    top: 0;
    left: 37px;
  }
  .banner__title {
    position: absolute;
    top: 41px;
    left: 0;
    margin: 0;
    font-weight: 800;
    font-size: 39px;
    white-space: nowrap;
  }
  .banner__tagline {
    position: absolute;
    top: 89px;
    left: 2px;
    margin: 0;
    font-weight: 500;
    font-size: 27px;
    white-space: nowrap;
  }
  .banner__cta {
    position: absolute;
    top: 152px;
    left: 0;
    width: 321px;
    height: 70px;
    border-radius: 35px;
    background: var(--orange);
    color: var(--white);
    font-weight: 800;
    font-size: 25px;
    display: flex;
    align-items: center;
    justify-content: center;
    text-decoration: none;
  }
  .features {
    position: absolute;
    top: 265px;
    left: 7px;
    margin: 0;
    padding: 0;
    list-style: none;
  }
  .features__item {
    display: flex;
    align-items: center;
    gap: 6px;
    height: 33px;
    padding: 0 20px 0 10px;
    margin-bottom: 16px;
    background: var(--white);
    border-radius: 17px;
    color: var(--ink);
    font-weight: 500;
    font-size: 18px;
    width: max-content;
  }
  .features__tick { width: 14px; height: 14px; }
</style>
</head>
<body>
  <section class="banner">
    <div class="banner__photo" role="img" aria-label="Security guard in a dark jacket shining a flashlight up a dim stairwell"></div>
    <div class="banner__brand">BRISK GUARD</div>

    <div class="banner__content">
      <h1 class="banner__title">GET SECURED TODAY</h1>
      <p class="banner__tagline">We take your security personal.</p>
      <a class="banner__cta" href="https://b.plomvarn.com">GET STARTED &gt;&gt;</a>

      <ul class="features">
        <li class="features__item">
          <svg class="features__tick" viewBox="0 0 14 14"><path d="M2 7.5 L5.5 11 L12 3.5" fill="none" stroke="#f6a623" stroke-width="2.6" stroke-linecap="round" stroke-linejoin="round"/></svg>
          Client Portal
        </li>
        <li class="features__item">
          <svg class="features__tick" viewBox="0 0 14 14"><path d="M2 7.5 L5.5 11 L12 3.5" fill="none" stroke="#f6a623" stroke-width="2.6" stroke-linecap="round" stroke-linejoin="round"/></svg>
          24x7 Dispatch
        </li>
        <li class="features__item">
          <svg class="features__tick" viewBox="0 0 14 14"><path d="M2 7.5 L5.5 11 L12 3.5" fill="none" stroke="#f6a623" stroke-width="2.6" stroke-linecap="round" stroke-linejoin="round"/></svg>
          No Binding Contracts
        </li>
      </ul>
    </div>
  </section>
</body>
</html>
```